Business Card Design

Stronger Living Compact for the Plains is a partnership of twenty different health organisations in the western suburbs of Melbourne, working together to improve the health of the local community. The western suburbs of Melbourne is one of the fastest growing and most culturally diverse populations in Australia and its communities have some of the poorest health outcomes in Australia.
Please see location for copy of the SLCP:
http://kvrt.com.au/fileadmin/filemount/pdf_files/SLCFTP_13_FINAL_JUNE_2012.pdf

Reason: Hello. I've extended the deadline because in the brief I made a confusing mention about a logo, but I actually meant the 'Stronger Living Compact for the Plains' jpg that I had already attached. Sorry about the confusion Thanks Fiona

Hello, Thanks for the designs I have already received. I have extended the deadline because I made a confusing reference to a logo in my brief, but I was talking about the 'Stronger Living Compact for the Plains' jpg I had already attached. There is no other logo for me to provide.

Thanks, Fiona

Target Market(s)

Health and state/local government managers and CEOs

Industry/Entity Type

Health

Contact Information for Business Card

Fiona Tremblay
Executive Officer
Stronger Living Compact for the Plains
Ph: 0438 592 614
Fiona.Tremblay@qn.org.au

Requirements
Must have
• logo and details as provided.
Would prefer matt finish
I can't see that logo has successfully attached so if it has not, please email or call me to follow up.

```html
<!DOCTYPE html>
<html lang="en">
<head>
<meta charset="utf-8">
<title>Stronger Living Compact for the Plains – Business Card</title>
<link rel="stylesheet" href="https://fonts.googleapis.com/css2?family=Caveat:wght@400;500&family=Questrial&display=swap">
<style>
  :root {
    --page: #ffffff;
    --card-front: #1090cf;
    --card-back: #4096d6;
    --ornament-tone: #63a9cc;
    --heart-tone: #f3e7a8;
    --text-light: #ffffff;
    --label-blue: #1a8ccd;
  }
  html, body {
    margin: 0;
    padding: 0;
    overflow: hidden;
    background: var(--page);
  }
  .canvas {
    position: relative;
    width: 1200px;
    height: 1072px;
    background: var(--page);
    overflow: hidden;
  }
  .card {
    position: absolute;
    left: 132px;
    width: 531px;
    height: 326px;
    overflow: hidden;
  }
  .card--front { top: 78px; background: var(--card-front); }
  .card--back  { top: 601px; background: var(--card-back); }

  .brand-name {
    position: absolute;
    left: 40px;
    top: 142px;
    margin: 0;
    font-family: "Questrial", sans-serif;
    font-weight: 400;
    font-size: 27px;
    line-height: 27.5px;
    color: var(--text-light);
    letter-spacing: 0.2px;
  }
  .flourish-area {
    position: absolute;
    left: 175px;
    top: 8px;
    width: 350px;
    height: 305px;
    border-radius: 50% 40% 30% 50%;
    background: radial-gradient(ellipse at 65% 55%, var(--ornament-tone) 0%, rgba(99,169,204,0.55) 45%, rgba(99,169,204,0) 72%);
    opacity: 0.8;
  }

  .contact {
    position: absolute;
    inset: 0;
    text-align: center;
    font-family: "Caveat", cursive;
    color: var(--text-light);
  }
  .contact__name {
    position: absolute;
    left: 0; right: 0;
    top: 44px;
    margin: 0;
    font-size: 33px;
    font-weight: 400;
    font-style: italic;
  }
  .contact__role {
    position: absolute;
    left: 0; right: 0;
    top: 88px;
    margin: 0;
    font-size: 23px;
    font-style: italic;
  }
  .heart-area {
    position: absolute;
    left: 156px;
    top: 134px;
    width: 218px;
    height: 76px;
    border-radius: 40% 40% 50% 50%;
    background: radial-gradient(ellipse at 50% 50%, rgba(243,231,168,0.35) 0%, rgba(243,231,168,0) 70%);
  }
  .contact__phone,
  .contact__email {
    position: absolute;
    left: 0; right: 0;
    margin: 0;
    font-size: 19px;
    font-style: italic;
  }
  .contact__phone { top: 225px; }
  .contact__email { top: 253px; }

  .side-label {
    position: absolute;
    left: 752px;
    margin: 0;
    font-family: "Caveat", cursive;
    font-weight: 500;
    font-style: italic;
    font-size: 190px;
    line-height: 1;
    color: var(--label-blue);
  }
  .side-label--front { top: 128px; }
  .side-label--back  { top: 652px; }
</style>
</head>
<body>
<div class="canvas">
  <section class="card card--front" aria-label="Business card front">
    <div class="flourish-area" role="img" aria-label="Faint swirling floral flourish in pale blue"></div>
    <p class="brand-name">Stronger<br>Living<br>Compact<br>for the<br>Plains</p>
  </section>
  <p class="side-label side-label--front">Front</p>

  <section class="card card--back" aria-label="Business card back">
    <div class="contact">
      <h1 class="contact__name">Fiona Tremblay</h1>
      <p class="contact__role">Executive Officer Stronger Living Compact for the Plains</p>
      <div class="heart-area" role="img" aria-label="Thin cream line ornament of intertwined hearts with curling sides"></div>
      <p class="contact__phone">Ph: 0438 592 614</p>
      <p class="contact__email">Fiona.Tremblay@qn.org.au</p>
    </div>
  </section>
  <p class="side-label side-label--back">Back</p>
</div>
</body>
</html>
```